Business Card Design

We need a business card design for an existing business. Our main trading brand is www.brightquillsaver.co.uk

We attach various logo files - please use the version that will produce the sharpest image on the business card.

We are flexible about shape of card etc. Please think outside the box as to what goes on front and what goes on back of the card

We want to be able to amend the card (once the design has been agreed ) to add additional staff details, but the text to go on it will be generic

Details to go on card ( for the first generic one) are fairly minimal as we don't like cluttered business cards:-

Neil Cathcart
Managing Director

Mobile: 07841 258 407
Email: n.cathcart@brightquillsaver.co.uk

Industry/Entity Type

Business

```html
<!DOCTYPE html>
<html lang="en">
<head>
<meta charset="utf-8">
<title>Brightquillsaver Business Card</title>
<link href="https://fonts.googleapis.com/css2?family=Lato:wght@400;700&family=Lora:ital@1&display=swap" rel="stylesheet">
<style>
  :root {
    --backdrop: #b8b9bb;
    --card: #fbfbfb;
    --brand-blue: #2c86c2;
    --brand-light: #8ccbef;
    --contact-navy: #1f4f78;
    --name-grey: #9b9b9b;
    --shadow: rgba(0, 0, 0, 0.22);
  }
  * { box-sizing: border-box; margin: 0; padding: 0; }
  html, body {
    width: 1200px;
    height: 750px;
    overflow: hidden;
  }
  body {
    background: var(--backdrop);
    font-family: "Lato", Arial, sans-serif;
  }
  .card-row {
    position: absolute;
    left: 259px;
    top: 259px;
    display: flex;
    align-items: flex-start;
  }
  .panel {
    height: 232px;
    background: var(--card);
    box-shadow: 0 3px 6px var(--shadow);
    position: relative;
  }
  .panel--brand-face {
    width: 228px;
    border-radius: 6px 116px 116px 6px;
    margin-right: 4px;
    display: flex;
    flex-direction: column;
    align-items: center;
    justify-content: center;
    padding-right: 20px;
    gap: 14px;
  }
  .brand-dot {
    width: 56px;
    height: 56px;
    border-radius: 50%;
    background: var(--brand-light);
  }
  .brand-face-name {
    font-size: 17px;
    color: var(--brand-blue);
    font-weight: 400;
  }
  .panel--contact-face {
    width: 380px;
    border-radius: 116px;
    margin-right: 66px;
  }
  .wordmark {
    position: absolute;
    left: 0;
    right: 0;
    top: 96px;
    display: flex;
    justify-content: center;
    align-items: center;
    gap: 10px;
  }
  .wordmark-name {
    font-size: 24px;
    font-weight: 400;
    color: var(--brand-blue);
    letter-spacing: 0.2px;
  }
  .wordmark-dot {
    width: 14px;
    height: 14px;
    border-radius: 50%;
    background: var(--brand-light);
  }
  .contact-list {
    position: absolute;
    left: 0;
    right: 0;
    top: 176px;
    list-style: none;
    text-align: center;
    font-size: 13px;
    color: var(--contact-navy);
    line-height: 20px;
  }
  .contact-list svg {
    vertical-align: -1px;
    margin-right: 5px;
  }
  .panel--name-face {
    width: 204px;
    border-radius: 4px 116px 116px 4px;
  }
  .person {
    position: absolute;
    left: 26px;
    top: 94px;
    text-align: right;
  }
  .person-name {
    font-family: "Lora", Georgia, serif;
    font-style: italic;
    font-size: 28px;
    color: var(--name-grey);
    text-shadow: 0 1px 0 #fff, 0 -1px 0 rgba(0,0,0,0.08);
    white-space: nowrap;
  }
  .person-title {
    font-family: "Lora", Georgia, serif;
    font-size: 10px;
    color: var(--name-grey);
  }
</style>
</head>
<body>
  <main class="card-row">
    <section class="panel panel--brand-face">
      <div class="brand-dot"></div>
      <p class="brand-face-name">brightquillsaver</p>
    </section>

    <section class="panel panel--contact-face">
      <div class="wordmark">
        <span class="wordmark-name">brightquillsaver.co.uk</span>
        <span class="wordmark-dot"></span>
      </div>
      <ul class="contact-list">
        <li>
          <svg width="8" height="12" viewBox="0 0 8 12" aria-hidden="true"><rect x="0.75" y="0.75" width="6.5" height="10.5" rx="1.2" fill="none" stroke="#2c86c2" stroke-width="1.5"/><rect x="3" y="9" width="2" height="1" fill="#2c86c2"/></svg>07841 258 407
        </li>
        <li>
          <svg width="12" height="9" viewBox="0 0 12 9" aria-hidden="true"><rect width="12" height="9" rx="1" fill="#2c86c2"/><path d="M0.5 0.8 L6 5 L11.5 0.8" fill="none" stroke="#fff" stroke-width="1"/></svg>n.cathcart@brightquillsaver.co.uk
        </li>
      </ul>
    </section>

    <section class="panel panel--name-face">
      <div class="person">
        <p class="person-name">Neil Cathcart</p>
        <p class="person-title">M.D.</p>
      </div>
    </section>
  </main>
</body>
</html>
```